Wheels for Elders Website Design

We need a NEW design and uploaded to Hostquill.com. Here is the current site: http://www.wheelsforelders.org

Need a form like this:

https://youthautogifts.org/

```html
<!DOCTYPE html>
<html lang="en">
<head>
<meta charset="utf-8">
<title>Wheels for Elders – Car Donation Made Easy</title>
<link rel="stylesheet" href="https://fonts.googleapis.com/css2?family=Lato:wght@300;400;700;900&display=swap">
<style>
:root{
  --red:#d0021b;
  --navy:#1b2a86;
  --ink:#2b2b2b;
  --muted:#6b6b6b;
  --line:#cfcfcf;
  --band:#eef1f5;
  --blue:#3a6fc2;
  --blue-light:#5d92d8;
  --white:#fff;
  --footer:#eef0f3;
}
*{box-sizing:border-box;margin:0;padding:0}
html,body{width:1200px;height:3879px;overflow:hidden;background:var(--white)}
body{font-family:"Lato",sans-serif;color:var(--ink);position:relative}
.abs{position:absolute}

/* header */
.site-header{position:absolute;left:0;top:0;width:1200px;height:116px;background:var(--white)}
.brand{position:absolute;display:flex;align-items:center;gap:14px;font-weight:900;color:var(--red);letter-spacing:.5px}
.brand-dot{width:38px;height:38px;border-radius:50%;background:var(--red)}
.header-brand{left:63px;top:38px;font-size:30px}
.header-call{position:absolute;right:111px;top:12px;font-size:19px;color:var(--ink);display:flex;align-items:center;gap:8px}
.header-call b{color:var(--red);font-size:23px;font-weight:700}
.main-nav{position:absolute;left:434px;top:62px;display:flex;gap:21px;font-size:18px}
.btn-red{background:var(--red);color:var(--white);font-weight:700;display:flex;align-items:center;justify-content:center;border-radius:3px}
.header-cta{position:absolute;left:914px;top:45px;width:175px;height:60px;font-size:20px}

/* hero */
.hero{position:absolute;left:0;top:116px;width:1200px;height:586px;background:linear-gradient(100deg,#8b8d7a 0%,#9a8f86 30%,#b9a9a4 45%,#a9c5de 60%,#8fbbe3 100%)}
.hero-title{position:absolute;left:706px;top:105px;font-size:66px;line-height:70px;font-weight:700;color:var(--white)}
.hero-sub{position:absolute;left:706px;top:266px;font-size:30px;color:var(--white)}
.hero-btn{position:absolute;left:705px;top:339px;width:179px;height:62px;background:var(--white);font-weight:900;font-size:19px;display:flex;align-items:center;justify-content:center;border-radius:3px}

/* donation form */
.donate-card{position:absolute;left:113px;top:602px;width:974px;height:482px;background:var(--white);box-shadow:0 4px 16px rgba(0,0,0,.14);border-radius:4px}
.steps{position:absolute;left:306px;top:30px;display:flex;align-items:center;gap:12px;font-size:20px}
.step-num{width:36px;height:36px;border-radius:50%;display:flex;align-items:center;justify-content:center;color:var(--white);font-weight:700}
.step-on .step-num{background:var(--navy)}
.step-on{color:var(--navy);display:flex;align-items:center;gap:12px}
.step-off .step-num{background:#bdbdbd}
.step-off{color:#a8a8a8;display:flex;align-items:center;gap:12px}
.step-line{width:36px;height:1px;background:#bdbdbd}
.field{position:absolute;width:288px}
.field label{display:block;font-size:18px;margin-bottom:14px}
.select{height:39px;border:1px solid var(--line);font-size:15px;color:var(--muted);display:flex;align-items:center;padding-left:12px;position:relative}
.select.has-arrow::after{content:"";position:absolute;right:0;top:0;width:40px;height:37px;border-left:1px solid var(--line)}
.select svg{position:absolute;right:14px;top:14px}
.form-btn{position:absolute;left:333px;top:303px;width:308px;height:63px;font-size:20px}
.trust{position:absolute;top:391px;width:60px;height:60px;border-radius:50%}

/* how to */
.section-title{position:absolute;left:0;width:1200px;text-align:center;font-size:42px;font-weight:400;color:var(--ink)}
.step-col{position:absolute;width:360px;text-align:center}
.step-icon{width:128px;height:128px;margin:0 auto;border-radius:8px;background:#e6ebf6}
.step-badge{width:46px;height:46px;border:2px solid #555;border-radius:50%;margin:20px auto 0;font-size:24px;display:flex;align-items:center;justify-content:center}
.step-col h3{font-size:28px;font-weight:400;margin-top:10px}
.step-col p{font-size:17px;line-height:29px;color:#555;margin-top:8px}

/* impact */
.impact{position:absolute;left:0;top:1566px;width:1200px;height:565px;background:var(--band)}
.card{position:absolute;top:127px;width:311px;height:381px;background:var(--white);border:1px solid #dedede;box-shadow:0 1px 5px rgba(0,0,0,.1);text-align:center}
.card-photo{margin:6px;height:181px}
.card h3{font-size:25px;font-weight:400;margin-top:26px}
.card p{font-size:16px;line-height:27px;color:#777;margin-top:6px}
.card a{display:block;color:var(--red);font-weight:700;font-size:17px;text-decoration:none;margin-top:10px}

/* why */
.why{position:absolute;left:0;top:2131px;width:1200px;height:581px;background:linear-gradient(90deg,var(--blue) 0%,var(--blue-light) 55%)}
.why-photo{position:absolute;left:617px;top:0;width:583px;height:581px;background:linear-gradient(160deg,#6e98cf 0%,#a99478 45%,#8b7a5e 100%)}
.why h2{position:absolute;left:109px;top:76px;font-size:45px;font-weight:700;color:var(--white)}
.why ul{position:absolute;left:109px;top:165px;list-style:none;width:560px}
.why li{position:relative;padding-left:28px;font-size:16px;line-height:28px;color:#e9f0fb;margin-bottom:26px}
.why li b{font-weight:700;color:var(--white);font-size:18px}
.why li svg{position:absolute;left:0;top:6px}

/* faq */
.faq{position:absolute;left:167px;width:866px;border:1px solid #c9c9c9;border-radius:3px;background:var(--white)}
.faq h4{font-size:21px;font-weight:400;padding:0 31px;line-height:52px}
.faq svg{position:absolute;right:24px;top:22px}
.faq p{font-size:16px;line-height:27px;color:#666;padding:0 31px 10px}

/* footer */
.site-footer{position:absolute;left:0;top:3453px;width:1200px;height:426px;background:var(--footer)}
.footer-brand{left:114px;top:62px;font-size:30px}
.footer-about{position:absolute;left:110px;top:150px;width:350px;font-size:16px;line-height:28px;color:#666}
.footer-call{position:absolute;left:470px;top:72px;width:416px;text-align:center;color:#555}
.footer-call .t{font-size:19px}
.footer-call .num{font-size:33px;font-weight:700;color:var(--red);margin-top:8px;display:flex;align-items:center;justify-content:center;gap:10px}
.footer-call .ops{font-size:19px;margin-top:14px}
.seal{position:absolute;top:214px;width:56px;height:44px;border-radius:6px;background:#d7dbe2}
.quick{position:absolute;left:902px;top:62px}
.quick h5{font-size:22px;font-weight:400;color:#444;margin-bottom:10px}
.quick a{display:block;font-size:16px;line-height:28px;color:#666;text-decoration:none}
.footer-rule{position:absolute;left:110px;top:335px;width:980px;height:1px;background:#d3d6db}
.copyright{position:absolute;left:110px;top:364px;font-size:15px;color:#666}
.social{position:absolute;top:355px;width:42px;height:42px;border-radius:50%;border:1px solid var(--red)}
</style>
</head>
<body>

<header class="site-header">
  <div class="brand header-brand"><span class="brand-dot"></span>WHEELS FOR ELDERS</div>
  <div class="header-call">
    <svg width="16" height="16" viewBox="0 0 24 24"><path fill="#d0021b" d="M6.6 10.8a15 15 0 0 0 6.6 6.6l2.2-2.2c.3-.3.7-.4 1-.2 1.1.4 2.3.6 3.6.6.6 0 1 .4 1 1V20c0 .6-.4 1-1 1A17 17 0 0 1 3 4c0-.6.4-1 1-1h3.5c.6 0 1 .4 1 1 0 1.3.2 2.5.6 3.6.1.3 0 .7-.2 1z"/></svg>
    Call Today to Donate <b>1-888-555-0142</b>
  </div>
  <nav class="main-nav"><span>About</span><span>How to Donate</span><span>Why Donate</span><span>FAQs</span><span>Contact</span></nav>
  <div class="btn-red header-cta">DONATE A CAR</div>
</header>

<section class="hero" role="img" aria-label="Photo of a soldier in camouflage holding a baby against a sky background">
  <h1 class="hero-title">Car Donation<br>Made Easy</h1>
  <p class="hero-sub">Join our 500,000+ donors</p>
  <div class="hero-btn">JOIN US NOW!</div>
</section>

<section class="donate-card">
  <div class="steps">
    <div class="step-on"><span class="step-num">1</span>Vehicle info</div>
    <span class="step-line"></span>
    <div class="step-off"><span class="step-num">2</span>Contact Info</div>
  </div>
  <div class="field" style="left:36px;top:88px"><label>Year</label><div class="select has-arrow">Select Year<svg width="12" height="8" viewBox="0 0 12 8"><path d="M1 1l5 5 5-5" fill="none" stroke="#666" stroke-width="1.5"/></svg></div></div>
  <div class="field" style="left:345px;top:88px"><label>Make</label><div class="select has-arrow">Select Make<svg width="12" height="8" viewBox="0 0 12 8"><path d="M1 1l5 5 5-5" fill="none" stroke="#666" stroke-width="1.5"/></svg></div></div>
  <div class="field" style="left:650px;top:88px"><label>Model</label><div class="select has-arrow">Select Model<svg width="12" height="8" viewBox="0 0 12 8"><path d="M1 1l5 5 5-5" fill="none" stroke="#666" stroke-width="1.5"/></svg></div></div>
  <div class="field" style="left:36px;top:191px"><label>Mileage</label><div class="select">Enter Mileage</div></div>
  <div class="field" style="left:345px;top:191px"><label>Does It Run?</label><div class="select has-arrow">Select<svg width="12" height="8" viewBox="0 0 12 8"><path d="M1 1l5 5 5-5" fill="none" stroke="#666" stroke-width="1.5"/></svg></div></div>
  <div class="field" style="left:650px;top:191px"><label>Title Available?</label><div class="select has-arrow">Select<svg width="12" height="8" viewBox="0 0 12 8"><path d="M1 1l5 5 5-5" fill="none" stroke="#666" stroke-width="1.5"/></svg></div></div>
  <div class="btn-red form-btn">DONATE MY VEHICLE NOW!</div>
  <span class="trust" style="left:364px;background:#f38a2f"></span>
  <span class="trust" style="left:457px;background:#b9bcc2"></span>
  <span class="trust" style="left:541px;background:#14a3a3"></span>
</section>

<h2 class="section-title" style="top:1138px">How to Donate</h2>
<div class="step-col" style="left:52px;top:1205px">
  <div class="step-icon" role="img" aria-label="Line icon of a form being filled in"></div>
  <div class="step-badge">1</div>
  <h3>Contact Us</h3>
  <p>Call us at 1-800-555-0199 or<br>Fill out the online form</p>
</div>
<div class="step-col" style="left:420px;top:1205px">
  <div class="step-icon" role="img" aria-label="Line icon of a tow hook lifting a car"></div>
  <div class="step-badge">2</div>
  <h3>Schedule Pickup</h3>
  <p>We'll call you today to arrange a convenient<br>pickup time for your car donation.</p>
</div>
<div class="step-col" style="left:789px;top:1205px">
  <div class="step-icon" role="img" aria-label="Line icon of scissors cutting a tax tag"></div>
  <div class="step-badge">3</div>
  <h3>Tax Deduction</h3>
  <p>You receive a tax receipt and<br>vacation voucher</p>
</div>

<section class="impact">
  <h2 class="section-title" style="top:43px">Your Car Impacts Veterans' Lives</h2>
  <article class="card" style="left:111px">
    <div class="card-photo" role="img" aria-label="Photo of a military family with a flag" style="background:linear-gradient(90deg,#8f7a6a,#c9b8a8,#7f8066)"></div>
    <h3>Help Us Reach Our Goal</h3>
    <p>Sed ut perspiciatis unde omnis is<br>te natus error sit voluptatem accusan<br>tium doloremque laudanti</p>
    <a>JOIN US</a>
  </article>
  <article class="card" style="left:445px">
    <div class="card-photo" role="img" aria-label="Photo of a smiling young woman leaning on a car" style="background:linear-gradient(160deg,#d9d2c9,#c9a988,#c45a3a)"></div>
    <h3>Vision</h3>
    <p>Sed ut perspiciatis unde omnis is<br>te natus error sit voluptatem accusan<br>tium doloremque laudanti</p>
    <a>ABOUT US</a>
  </article>
  <article class="card" style="left:778px">
    <div class="card-photo" role="img" aria-label="Photo of volunteers stacking hands together" style="background:linear-gradient(180deg,#8a5a4a,#b07e66,#5a6e3a)"></div>
    <h3>On The Field</h3>
    <p>Sed ut perspiciatis unde omnis is<br>te natus error sit voluptatem accusan<br>tium doloremque laudanti</p>
    <a>VOLUNTEER</a>
  </article>
</section>

<section class="why">
  <div class="why-photo" role="img" aria-label="Photo of a child hugging a soldier holding a small flag"></div>
  <h2>Why Donate Your Car To Us</h2>
  <ul>
    <li><svg width="16" height="16" viewBox="0 0 16 16"><circle cx="8" cy="8" r="8" fill="#fff"/><path d="M4.5 8.2l2.3 2.3 4.7-4.8" fill="none" stroke="#3a6fc2" stroke-width="2"/></svg><b>IRS 501(c)3 Approved :</b> Free 24/7 Pickup with No DMV Hassles.</li>
    <li><svg width="16" height="16" viewBox="0 0 16 16"><circle cx="8" cy="8" r="8" fill="#fff"/><path d="M4.5 8.2l2.3 2.3 4.7-4.8" fill="none" stroke="#3a6fc2" stroke-width="2"/></svg><b>Free Local Towing :</b> We will pick up your car donation, running or not, when it's most convenient, at home or work.</li>
    <li><svg width="16" height="16" viewBox="0 0 16 16"><circle cx="8" cy="8" r="8" fill="#fff"/><path d="M4.5 8.2l2.3 2.3 4.7-4.8" fill="none" stroke="#3a6fc2" stroke-width="2"/></svg><b>Income Tax Deduction :</b> We issue you an IRS tax receipt and get you the highest tax write-off possible.</li>
    <li><svg width="16" height="16" viewBox="0 0 16 16"><circle cx="8" cy="8" r="8" fill="#fff"/><path d="M4.5 8.2l2.3 2.3 4.7-4.8" fill="none" stroke="#3a6fc2" stroke-width="2"/></svg><b>No Paperwork Hassles :</b> We handle everything: DMV and IRS paperwork.</li>
    <li><svg width="16" height="16" viewBox="0 0 16 16"><circle cx="8" cy="8" r="8" fill="#fff"/><path d="M4.5 8.2l2.3 2.3 4.7-4.8" fill="none" stroke="#3a6fc2" stroke-width="2"/></svg><b>Schedule a Free Pickup :</b> Complete the form and a representative will call you to arrange a convenient time to pickup your car.</li>
  </ul>
</section>

<h2 class="section-title" style="top:2758px">Frequently Asked Questions</h2>
<div class="faq" style="top:2842px;height:131px">
  <h4 style="line-height:66px">What types of vehicles can be donated?</h4>
  <svg width="14" height="9" viewBox="0 0 14 9"><path d="M1 8l6-6 6 6" fill="none" stroke="#555" stroke-width="1.6"/></svg>
  <p style="margin-top:-12px">Nemo enim ipsam voluptatem quia voluptas sit aspernatur aut odit aut fugit, sed quia consequuntur<br>magni dolores eos qui ratione voluptat eque porro quisquam est, qui.</p>
</div>
<div class="faq" style="top:2986px"><h4>hat paperwork do I need to donate my vehicle?</h4><svg width="14" height="9" viewBox="0 0 14 9"><path d="M1 1l6 6 6-6" fill="none" stroke="#555" stroke-width="1.6"/></svg></div>
<div class="faq" style="top:3055px"><h4>Is my donated vehicle tax-deductible?</h4><svg width="14" height="9" viewBox="0 0 14 9"><path d="M1 1l6 6 6-6" fill="none" stroke="#555" stroke-width="1.6"/></svg></div>
<div class="faq" style="top:3123px"><h4>What if the vehicle is not registered in my name?</h4><svg width="14" height="9" viewBox="0 0 14 9"><path d="M1 1l6 6 6-6" fill="none" stroke="#555" stroke-width="1.6"/></svg></div>
<div class="faq" style="top:3192px"><h4>How much will I receive as a tax deduction for my vehicle?</h4><svg width="14" height="9" viewBox="0 0 14 9"><path d="M1 1l6 6 6-6" fill="none" stroke="#555" stroke-width="1.6"/></svg></div>
<div class="faq" style="top:3260px"><h4>When will I receive my tax receipt?</h4><svg width="14" height="9" viewBox="0 0 14 9"><path d="M1 1l6 6 6-6" fill="none" stroke="#555" stroke-width="1.6"/></svg></div>
<div class="faq" style="top:3329px"><h4>How do I schedule a pick up?</h4><svg width="14" height="9" viewBox="0 0 14 9"><path d="M1 1l6 6 6-6" fill="none" stroke="#555" stroke-width="1.6"/></svg></div>

<footer class="site-footer">
  <div class="brand footer-brand"><span class="brand-dot"></span>WHEELS FOR ELDERS</div>
  <p class="footer-about">Offers support and/or financial assistance to veterans and active military personal and/or their family members who become newly blind and/or visually impaired from age-related macular degeneration, retinitis pigmentosa, glaucoma, keratoconus or diabetic retinopathy.</p>
  <div class="footer-call">
    <div class="t">Call Today To Donate</div>
    <div class="num"><svg width="26" height="26" viewBox="0 0 24 24"><path fill="#d0021b" d="M6.6 10.8a15 15 0 0 0 6.6 6.6l2.2-2.2c.3-.3.7-.4 1-.2 1.1.4 2.3.6 3.6.6.6 0 1 .4 1 1V20c0 .6-.4 1-1 1A17 17 0 0 1 3 4c0-.6.4-1 1-1h3.5c.6 0 1 .4 1 1 0 1.3.2 2.5.6 3.6.1.3 0 .7-.2 1z"/></svg>1-800-555-0199</div>
    <div class="ops">Live Operators Available - 7 Days A Week</div>
  </div>
  <span class="seal" style="left:582px;width:100px"></span>
  <span class="seal" style="left:717px;width:54px;height:54px;border-radius:50%;top:210px"></span>
  <nav class="quick">
    <h5>Quick Links</h5>
    <a>How To Donate</a><a>Why Donate</a><a>FAQ</a><a>About</a>
  </nav>
  <div class="footer-rule"></div>
  <p class="copyright">Copyright ©2020. WHEELS FOR ELDERS. All rights reserved.</p>
  <span class="social" style="left:891px"></span>
  <span class="social" style="left:942px"></span>
  <span class="social" style="left:994px"></span>
  <span class="social" style="left:1046px"></span>
</footer>

</body>
</html>
```